Website Design for Freeze-Dried Food Manufacturing Company (Pet Food & Agri-Food)

We are looking for a high-level web designer to create a clean, modern, premium website design for Brindle, a freeze-dried food manufacturing company operating in both the pet food and agri-food space.
This is not a basic website build β we are looking for a designer who understands brand positioning, layout, and user flow, not just visuals.
π― Project Objective
Design a website that:
Clearly communicates our capabilities and value proposition
Feels premium, credible, and product-driven
Guides users through a simple, intuitive journey
Clean and Crips
A critical requirement is clearly separating:
π Pet Food
π Agri-Food
These must feel like two distinct pathways within the same brand experience.
We have attached detailed documents outlining structure, layout, and messaging. These should be followed closely.
π What Success Looks Like
A high-impact homepage with strong visual hierarchy
Clear entry points into Pet Food and Agri-Food
Clean, intentional layout (not cluttered or template-like)
Thoughtful spacing, typography, and flow
A design that feels considered and elevated, not generic
π¨ Design Direction
We are aiming for a:
Minimal, premium aesthetic
Warm, natural color palette (creams, browns, muted tones)
Ingredient and product-focused visuals
Avoid:
Overly corporate / industrial styles
Generic SaaS-style layouts
Busy or over-designed interfaces
End Goal
A website that immediately communicates:
Who we are
What we do
Why weβre different
In a way that feels premium, clear, and easy to navigate.
Link to current website: https://brindleharvest.example/
https://brindlelabs.example/wp-admin/

```html
<!DOCTYPE html>
<html lang="en">
<head>
<meta charset="utf-8">
<title>Brindle — Nutrition, Frozen in Time</title>
<link href="https://fonts.googleapis.com/css2?family=Playfair+Display:ital,wght@0,400;0,500;0,600;0,700;1,500;1,600;1,700&family=Inter:wght@400;500;600;700&display=swap" rel="stylesheet">
<style>
:root{
  --cream:#f8f3ec;
  --cream-2:#f2e8de;
  --card:#fbf7f2;
  --ink:#2b231d;
  --muted:#7b6f66;
  --brown:#b58463;
  --brown-deep:#a4785a;
  --dark:#4a3d31;
  --line:#e8ddd1;
}
*{box-sizing:border-box;margin:0;padding:0}
html,body{width:1200px;height:4332px;overflow:hidden}
body{background:var(--cream);font-family:"Inter",sans-serif;color:var(--ink);position:relative}
.serif{font-family:"Playfair Display",serif}
section,header,footer{position:absolute;left:0;width:1200px}
.abs{position:absolute}
.center{left:0;width:1200px;text-align:center}
.eyebrow{display:inline-flex;align-items:center;gap:6px;padding:4px 12px;border-radius:20px;background:#efe4d8;color:#c4a389;font-size:8px;letter-spacing:2px;font-weight:600;text-transform:uppercase}
.chev{position:absolute;left:594px;width:12px;height:8px}

/* nav */
.nav{top:0;height:62px;background:var(--cream);border-bottom:1px solid var(--line);z-index:2}
.brand{position:absolute;left:151px;top:14px;font-family:"Playfair Display",serif;font-size:24px;color:var(--brown)}
.nav ul{position:absolute;right:291px;top:26px;display:flex;gap:20px;list-style:none;font-size:9px;letter-spacing:1px;color:#6b5e54;font-weight:500}
.nav .contact{position:absolute;left:972px;top:20px;width:81px;height:24px;background:var(--brown);color:#fff;font-size:9px;font-weight:600;letter-spacing:1px;display:flex;align-items:center;justify-content:center}

/* hero */
.hero{top:62px;height:518px;background:linear-gradient(100deg,#f7efe4 0%,#f3e4cf 45%,#ecd9bf 70%,#e9dcc6 100%);overflow:hidden}
.hero-bg{position:absolute;left:0;top:0;width:1200px;height:518px;background:radial-gradient(circle at 700px 330px,rgba(200,170,120,.35),transparent 60%)}
.hero .eyebrow{position:absolute;left:147px;top:60px}
.hero h1{position:absolute;left:147px;top:100px;font-family:"Playfair Display",serif;font-weight:600;font-size:74px;line-height:76px;color:var(--ink)}
.hero h1 em{color:var(--brown);font-style:italic;display:block}
.hero .sub{position:absolute;left:147px;top:268px;font-family:"Playfair Display",serif;font-size:18px;color:var(--ink)}
.hero .hrule{position:absolute;left:147px;top:316px;width:62px;height:2px;background:var(--brown)}
.hero p.lead{position:absolute;left:147px;top:344px;width:450px;font-size:15px;line-height:22px;color:#4e443c}
.btn{position:absolute;height:38px;display:flex;align-items:center;justify-content:center;gap:8px;font-size:9px;letter-spacing:1.3px;font-weight:700}
.btn-fill{background:var(--brown);color:#fff}
.btn-line{border:1px solid #d4c2ae;color:var(--ink)}
.hero-photo{position:absolute;left:790px;top:228px;width:348px;height:290px;border:4px solid #fff;border-bottom:none;background:conic-gradient(from 200deg at 50% 100%,#d2a33c,#e2c987,#b9ad98,#4f7a3a,#7a3c2f,#9a4a3c,#c46b32,#d2a33c);box-shadow:0 10px 30px rgba(0,0,0,.15)}

/* split */
.split{top:580px;height:580px}
.pet{position:absolute;left:0;top:0;width:600px;height:580px;background:var(--brown-deep)}
.pet-photo{position:absolute;left:170px;top:190px;width:260px;height:260px;border-radius:50%;background:radial-gradient(circle,#8d5a3c,#6a4330 60%,#8a6a55);opacity:.9}
.agri{position:absolute;left:600px;top:0;width:600px;height:580px;background:#fbf8f4}
.agri-photo{position:absolute;left:150px;top:170px;width:320px;height:230px;background:linear-gradient(135deg,#8aa56a 0%,#d9c4a6 40%,#e28a3a 75%,#fbf8f4 100%);opacity:.55;border-radius:40% 60% 50% 50%}
.split h2{position:absolute;font-family:"Playfair Display",serif;font-weight:500;font-size:54px;text-align:center;width:600px}
.split p{position:absolute;font-size:14px;line-height:21px;text-align:center;width:230px}
.pill{position:absolute;left:504px;top:510px;width:192px;height:24px;border-radius:12px;background:#fff;border:1px solid var(--line);font-size:7.5px;letter-spacing:1.5px;color:var(--brown);font-weight:600;display:flex;align-items:center;justify-content:center}

/* standards */
.standards{top:1160px;height:578px;background:var(--cream)}
.std-card{position:absolute;top:228px;width:208px;height:274px;background:var(--card);border-radius:10px;box-shadow:0 4px 18px rgba(120,90,60,.06);text-align:center;padding:26px 20px 0}
.std-badge{width:74px;height:74px;border-radius:50%;background:#111;margin:0 auto 34px;display:flex;align-items:center;justify-content:center}
.std-card h3{font-family:"Playfair Display",serif;font-size:14px;font-weight:600;margin-bottom:14px;white-space:nowrap}
.std-card p{font-size:10.5px;line-height:17px;color:var(--muted)}

/* ecosystem */
.eco{top:1738px;height:580px;background:linear-gradient(180deg,#4a3c2f,#5b4a39 50%,#4a3c30);overflow:hidden;color:#fff}
.eco-bg{position:absolute;left:150px;top:60px;width:900px;height:700px;border-radius:50%;background:conic-gradient(#8a6f4a,#6b5033,#7a5b3e,#5e4b30,#6d4535,#5a4f35,#8a6f4a);opacity:.45}
.eco h2{font-family:"Playfair Display",serif;font-weight:500;font-size:50px;line-height:48px;color:var(--brown)}
.eco h2 em{color:#d8c09f;display:block;font-weight:600}
.step{position:absolute;top:362px;width:140px;text-align:center}
.step .num{width:38px;height:38px;border-radius:50%;background:#3a2f26;border:2px solid #5e4f41;margin:0 auto 28px;font-size:11px;display:flex;align-items:center;justify-content:center}
.step h4{font-family:"Playfair Display",serif;font-size:15px;font-weight:700;margin-bottom:8px}
.step p{font-size:10.5px;line-height:17px;color:#cdbfb0}

/* capabilities */
.caps{top:2318px;height:580px;background:var(--cream-2)}
.cap-card{position:absolute;top:218px;width:285px;height:284px;background:var(--card);border-radius:16px;padding:36px 36px}
.cap-icon{width:62px;height:62px;border-radius:8px;background:#f0e3d6;display:flex;align-items:center;justify-content:center;margin-bottom:28px}
.cap-card h3{font-family:"Playfair Display",serif;font-size:17px;font-weight:600;margin-bottom:20px}
.cap-card p{font-size:11.5px;line-height:20px;color:var(--muted)}

/* partners */
.partners{top:2898px;height:580px;background:var(--cream)}
.quote{position:absolute;left:440px;top:189px;width:280px;height:183px;background:#fff;border-radius:20px;box-shadow:0 14px 40px rgba(120,90,60,.14);padding:50px 24px 0}
.quote p{font-size:12px;line-height:20px;font-style:italic;color:#4e443c}
.quote .who{margin-top:16px;padding-left:38px;font-size:10px;font-weight:600}
.quote .who span{display:block;color:var(--brown);font-size:8px;letter-spacing:1px;margin-top:3px}
.orb{position:absolute;border-radius:50%;background:#fff;box-shadow:0 4px 14px rgba(0,0,0,.06);display:flex;align-items:center;justify-content:center}
.orb i{display:block;border-radius:4px;background:#d9d1c8}

/* cta */
.cta{top:3478px;height:580px;background:linear-gradient(180deg,#5d4b32,#705c3f 50%,#6a5a43);overflow:hidden}
.cta-bg{position:absolute;left:100px;top:120px;width:1000px;height:800px;border-radius:50%;background:conic-gradient(#a08a68,#8a6a47,#9a6a55,#7a5a40,#9a5a48,#8d7a55,#a08a68);opacity:.4}
.cta-card{position:absolute;left:265px;top:142px;width:671px;height:302px;border-radius:22px;background:rgba(120,100,80,.55);border:1px solid rgba(255,255,255,.12);text-align:center;color:#fff;padding-top:44px}
.cta-card h2{font-family:"Playfair Display",serif;font-size:34px;line-height:36px;font-weight:600}
.cta-card h2 em{color:#d4b58b;display:block;font-weight:500}
.cta-card p{width:510px;margin:28px auto 0;font-size:11.5px;line-height:19px;color:#e6dccf}
.cta-card .btn{position:absolute;top:236px;height:36px;border-radius:18px}

/* footer */
.foot{top:4058px;height:274px;background:var(--cream)}
.foot .brand{left:151px;top:44px;font-size:30px}
.foot h5{position:absolute;top:66px;font-family:"Playfair Display",serif;font-size:13px;letter-spacing:1.5px;color:var(--brown);font-weight:600}
.foot .about{position:absolute;left:147px;top:100px;width:210px;font-size:10.5px;line-height:16px;color:#4e443c}
.foot ul{position:absolute;left:383px;top:102px;list-style:none;font-size:10.5px;line-height:25px;color:#4e443c}
.foot .subtxt{position:absolute;left:619px;top:102px;width:200px;font-size:10px;line-height:16px;color:#4e443c}
.foot .field{position:absolute;left:619px;top:144px;width:198px;height:32px;background:#fff;border:1px solid var(--line);font-size:10px;color:#b2a597;padding:10px 12px}
.soc{position:absolute;top:115px;width:28px;height:28px;border-radius:50%;background:#efe4d8}
.copy{position:absolute;top:252px;font-size:9px;letter-spacing:1px;color:#a79a8c}
</style>
</head>
<body>

<header class="nav">
  <div class="brand">Brindle</div>
  <ul><li>OUR STORY</li><li>PHARMA</li><li>PET FOOD</li><li>AGRI-FOOD</li><li>QUALITY</li></ul>
  <div class="contact">CONTACT</div>
</header>

<section class="hero">
  <div class="hero-bg" role="img" aria-label="Soft backdrop of freeze-dried ingredients arranged in a wheel"></div>
  <span class="eyebrow">● BRINDLE</span>
  <h1>Nutrition,<em>Frozen in Time</em></h1>
  <div class="sub">Industrial Freeze-Drying &amp; Food Manufacturing</div>
  <div class="hrule"></div>
  <p class="lead">A fully integrated, closed-loop system from ingredient sourcing through to production, packaging, and distribution.</p>
  <div class="btn btn-fill" style="left:147px;top:420px;width:172px">START A PROJECT
    <svg width="10" height="8" viewBox="0 0 10 8"><path d="M0 4h9M6 1l3 3-3 3" stroke="#fff" fill="none" stroke-width="1.2"/></svg></div>
  <div class="btn btn-line" style="left:335px;top:420px;width:152px">OUR CAPABILITIES</div>
  <div class="hero-photo" role="img" aria-label="Photo of grains, seeds, greens and meat arranged in wedges on a yellow surface"></div>
</section>

<section class="split">
  <div class="pet">
    <div class="pet-photo" role="img" aria-label="Bowl of freeze-dried pet food"></div>
    <h2 style="left:0;top:215px;color:#fff">Pet Food</h2>
    <p style="left:185px;top:308px;color:#fff">Human-grade ingredients, scalable freeze-drying, and specialized production for premium pet nutrition.</p>
  </div>
  <div class="agri">
    <div class="agri-photo" role="img" aria-label="Fresh carrot with leafy greens"></div>
    <h2 style="left:0;top:215px;color:var(--ink)">Agri-Food</h2>
    <p style="left:185px;top:308px;color:var(--ink)">Premium ingredients, botanical powders, and value-added agrifood formats — from farm to market.</p>
  </div>
  <div class="pill">● 4PL SUPPLY CHAIN PARTNER</div>
</section>

<section class="standards">
  <div class="abs center" style="top:76px"><span class="eyebrow">◎ COMPLIANCE &amp; QUALITY</span></div>
  <h2 class="abs center serif" style="top:104px;font-size:38px;font-weight:500">Certified Industry Standards</h2>
  <div class="abs" style="left:575px;top:164px;width:50px;height:2px;background:var(--brown)"></div>

  <div class="std-card" style="left:147px"><div class="std-badge" role="img" aria-label="Certification badge"></div><h3>Health Board Licensed</h3><p>Licensed by the National Health Board as a non-producer to store controlled substances.</p></div>
  <div class="std-card" style="left:380px"><div class="std-badge" role="img" aria-label="Certification badge"></div><h3>Food Authority Certified</h3><p>Safe Foods Standard certification issued by the Meridian Food Authority.</p></div>
  <div class="std-card" style="left:612px"><div class="std-badge"><svg width="30" height="34" viewBox="0 0 30 34"><path d="M15 2 27 7v9c0 8-5 13-12 16C8 29 3 24 3 16V7z" fill="none" stroke="#fff" stroke-width="2"/><rect x="10" y="15" width="10" height="8" rx="1" fill="#fff"/><path d="M12 15v-3a3 3 0 0 1 6 0v3" stroke="#fff" fill="none" stroke-width="1.6"/></svg></div><h3>4PL Supply Chain</h3><p>Providing complete supply chain solutions.</p></div>
  <div class="std-card" style="left:845px"><div class="std-badge"><svg width="20" height="36" viewBox="0 0 20 36"><rect x="7" y="2" width="6" height="22" rx="3" fill="none" stroke="#fff" stroke-width="1.8"/><circle cx="10" cy="28" r="6" fill="#fff"/><path d="M10 10v16" stroke="#fff" stroke-width="2"/></svg></div><h3>Cold Chain</h3><p>Environmentally-controlled storage, mechanical processing, freeze-drying, packaging and food-safety technologies.</p></div>
  <svg class="chev" style="top:544px" viewBox="0 0 12 8"><path d="M1 1l5 5 5-5" stroke="#b8a898" fill="none"/></svg>
</section>

<section class="eco">
  <div class="eco-bg" role="img" aria-label="Dim backdrop of ingredients arranged in a wheel"></div>
  <div class="abs center" style="top:64px"><span class="eyebrow" style="background:#3e3228;color:#c9a883">∿ OPERATIONAL EXCELLENCE</span></div>
  <h2 class="abs center" style="top:100px">A Complete,<em>Closed-Loop Ecosystem</em></h2>
  <p class="abs" style="left:300px;top:212px;width:600px;text-align:center;font-size:14px;line-height:22px;color:#ddd1c3">From raw ingredient sourcing to global distribution, our system ensures full traceability and efficiency.</p>
  <div class="step" style="left:147px"><div class="num">1</div><h4>Sourcing</h4><p>Direct from farmers &amp; certified suppliers.</p></div>
  <div class="step" style="left:300px"><div class="num">2</div><h4>R&amp;D</h4><p>Custom formulation &amp; test kitchen pilots.</p></div>
  <div class="step" style="left:453px"><div class="num">3</div><h4>Processing</h4><p>Industrial scale freeze-drying &amp; extraction.</p></div>
  <div class="step" style="left:606px"><div class="num">4</div><h4>Packaging</h4><p>Sachet, bulk, or retail-ready solutions.</p></div>
  <div class="step" style="left:759px"><div class="num">5</div><h4>Storage</h4><p>Cold chain &amp; controlled atmosphere.</p></div>
  <div class="step" style="left:913px"><div class="num" style="background:#2f261f;box-shadow:0 0 14px rgba(255,220,180,.3)">6</div><h4 style="color:#d4b58b">Logistics</h4><p>4PL distribution &amp; cross-border export.</p></div>
  <svg class="chev" style="top:542px" viewBox="0 0 12 8"><path d="M1 1l5 5 5-5" stroke="#9a8a78" fill="none"/></svg>
</section>

<section class="caps">
  <div class="abs center" style="top:80px"><span class="eyebrow" style="background:#eadccd">◎ OUR EXPERTISE</span></div>
  <h2 class="abs center serif" style="top:106px;font-size:38px;font-weight:500">Core Capabilities</h2>
  <div class="abs" style="left:575px;top:164px;width:50px;height:2px;background:var(--brown)"></div>
  <div class="cap-card" style="left:147px"><div class="cap-icon"><svg width="20" height="20" viewBox="0 0 20 20"><path d="M10 2 17 6v8l-7 4-7-4V6zM3 6l7 4 7-4M10 10v8" stroke="#b58463" fill="none" stroke-width="1.4"/></svg></div><h3>OEM / Private Label</h3><p>From concept to commercialization. We help you build your brand with our world-class manufacturing expertise.</p></div>
  <div class="cap-card" style="left:458px"><div class="cap-icon"><svg width="20" height="20" viewBox="0 0 20 20"><path d="M10 2v16M3 6l14 8M17 6 3 14" stroke="#b58463" stroke-width="1.4"/></svg></div><h3>Freeze Drying</h3><p>Industrial scale freeze-drying for food, ingredients, and agri-products. Preserving nutrition and flavor at scale.</p></div>
  <div class="cap-card" style="left:768px"><div class="cap-icon"><svg width="20" height="20" viewBox="0 0 20 20"><path d="M13 2l5 5-9 9H4v-5zM4 16l-2 2" stroke="#b58463" fill="none" stroke-width="1.4"/></svg></div><h3>R&amp;D Test Kitchen</h3><p>Pilot runs, formulation, and product optimization. Innovation is at the heart of everything we do.</p></div>
  <svg class="chev" style="top:544px" viewBox="0 0 12 8"><path d="M1 1l5 5 5-5" stroke="#b8a898" fill="none"/></svg>
</section>

<section class="partners">
  <div class="abs center" style="top:50px"><span class="eyebrow">◎ INDUSTRY NETWORK</span></div>
  <h2 class="abs center serif" style="top:82px;font-size:38px;font-weight:500">Partners in Innovation</h2>
  <div class="quote">
    <p>The quality of the pet treats is unmatched. Our customers love the consistency.</p>
    <div class="who">Coastline Food Guild<span>PARTNER</span></div>
  </div>
  <div class="orb" style="left:728px;top:245px;width:74px;height:74px;border:2px solid var(--brown)"><i style="width:40px;height:18px;background:#cfc4b8"></i></div>
  <div class="orb" style="left:290px;top:290px;width:50px;height:50px"><i style="width:30px;height:8px"></i></div>
  <div class="orb" style="left:468px;top:390px;width:50px;height:50px"><i style="width:30px;height:10px"></i></div>
  <div class="orb" style="left:243px;top:476px;width:46px;height:46px"><i style="width:36px;height:36px;border-radius:50%;background:#8d8782"></i></div>
  <div class="orb" style="left:922px;top:420px;width:50px;height:50px"><i style="width:30px;height:8px"></i></div>
  <svg class="chev" style="top:548px" viewBox="0 0 12 8"><path d="M1 1l5 5 5-5" stroke="#b8a898" fill="none"/></svg>
</section>

<section class="cta">
  <div class="cta-bg" role="img" aria-label="Warm backdrop of ingredient wedges"></div>
  <div class="cta-card">
    <span class="eyebrow" style="background:rgba(60,45,35,.5);color:#e2d2bd">▢ GET STARTED</span>
    <h2 style="margin-top:14px">Ready to Start<em>Your Project?</em></h2>
    <p>Whether you're in Pharma, Agrifood, or looking for 4PL supply chain management, our team is ready to optimize your midstream operations.</p>
    <div class="btn btn-fill" style="left:156px;width:206px">CONTACT US TODAY
      <svg width="10" height="8" viewBox="0 0 10 8"><path d="M0 4h9M6 1l3 3-3 3" stroke="#fff" fill="none" stroke-width="1.2"/></svg></div>
    <div class="btn" style="left:373px;width:141px;background:rgba(90,80,72,.8);color:#fff">LEARN MORE</div>
  </div>
</section>

<footer class="foot">
  <div class="brand">Brindle</div>
  <div class="about">AGRIFOOD, LIFE-SCIENCE &amp; PHARMACEUTICAL specialists. Providing midstream supply chain solutions with precision and integrity.</div>
  <h5 style="left:383px">QUICK LINKS</h5>
  <ul><li>About Us</li><li>Pharma &amp; Life-Science</li><li>Agrifood &amp; Pet Food</li><li>Logistics</li></ul>
  <h5 style="left:619px">SUBSCRIBE</h5>
  <div class="subtxt">Sign-up and subscribe to our email list to receive important updates!</div>
  <div class="field">Your email address
    <svg class="abs" style="right:10px;top:10px" width="12" height="12" viewBox="0 0 12 12"><path d="M1 6 11 1 8 11 6 7z" stroke="#b58463" fill="none"/></svg></div>
  <h5 style="left:855px">FOLLOW US</h5>
  <div class="soc" style="left:856px" aria-label="Social link"></div>
  <div class="soc" style="left:900px" aria-label="Social link"></div>
  <div class="soc" style="left:944px" aria-label="Social link"></div>
  <div class="copy center">© 2026 BRINDLE. ALL RIGHTS RESERVED. AGRIFOOD, LIFE-SCIENCE &amp; PHARMACEUTICAL SPECIALISTS.</div>
</footer>

</body>
</html>
```